Personal coach needs brochure design for inspirational essay about authenticity

Overview:
I want a beautiful brochure, 11”x17” that folds to 8-1/2”x11” with 4 pages. Think of it as an oversize greeting card.
• Front cover: photograph of a dancer and title with attribution of quote (Pixavanto jpeg photo attached)
• Inside spread: Copy (Edith Sorrel copy attached) with some appropriate illustration, based on cover photo
• Back cover: contact information, brief descriptive copy, two small photos (jpeg photo attached; see copy for direction)
Copy for front cover title, inside spread and back cover is attached in doc titled "Edith Sorrel copy"

Purpose of brochure:
I'm a personal coach and once a year I produce a 4-page illustrated inspirational essay, which invites personal reflection on living a more mindful, meaningful life. Most people I send them to collect them. Someday in the future I'd like to put a collection of these essays into a coffee table book and also create a website for the collection, which is related to the personal coaching that I do.
I have the brochures printed hard copy. I have attached a few examples from previous years. Each has a unique design related to its theme.

Concept:
This year’s essay theme, “There will only ever be one you!” is based on a quote by Edith Sorrel, a famous modern dancer. The complete quote, which appears in the copy, is about being true to one’s authentic self. The essay is not about dance, but because the author of the quote was a dancer who personified this theme of being unique to self, I have selected a photo of dance for the cover.

Design Guidance:
Front cover: One possibility is to expand the background color of the Pixavanto photo so the photo seems to emerge from the background. But I am open to ideas. I think the photo is artsy enough as it is, but there may be other ways to treat it (e.g. special effects) that would also work. The title should appear somewhere. Make the attribution (--Edith Sorrel) in smaller type than the title.

Inside Spread: There may be ways to borrow a design motif from the cover photo to make the inside spread more visually interesting, i.e., not just straight copy. I think it may be helpful to make the font size of the quote larger than the rest of the copy, but it has to be read in sequence. Or maybe it's printed in same size as copy, but then also repeated and displayed by itself in larger type.

Back cover: If you look at some of the other examples I’ve sent, you’ll see how the back cover is typically handled. I want a reduced version of the cover to be placed near the line that says "this is the 16th in a series.." Then, there’s a jpeg photo of Edith Sorrel that should be placed next to the copy description of her.

Need extra days to review

```html
<!DOCTYPE html>
<html lang="en">
<head>
<meta charset="utf-8">
<title>There Will Only Ever Be One You — Essay Brochure</title>
<link href="https://fonts.googleapis.com/css2?family=Poiret+One&family=Didact+Gothic&display=swap" rel="stylesheet">
<style>
  :root {
    --ink: #2a2a2a;
    --blue: #5b89b7;
    --blue-deep: #4f7fae;
    --band: #5a87b6;
    --night: #1d1e20;
    --night-soft: #3a3c40;
    --paper: #ffffff;
    --silk: #6f8fb5;
  }
  * { margin: 0; padding: 0; box-sizing: border-box; }
  html, body { width: 920px; height: 1200px; overflow: hidden; background: var(--paper); }
  body { position: relative; font-family: "Didact Gothic", sans-serif; color: var(--ink); }

  .display { font-family: "Poiret One", sans-serif; text-transform: uppercase; letter-spacing: 0.5px; line-height: 0.95; }

  /* ---------- Back cover ---------- */
  .back-cover { position: absolute; left: 0; top: 0; width: 460px; height: 595px; }
  .mini-cover {
    position: absolute; left: 44px; top: 38px; width: 162px; height: 206px;
    background: var(--night); transform: rotate(-4deg); padding: 22px 12px;
    box-shadow: 0 1px 3px rgba(0,0,0,.25);
  }
  .mini-cover .mini-title { font-size: 13px; color: var(--blue); }
  .mini-cover .mini-title span { color: #fff; }
  .mini-cover .mini-attr { font-family: "Poiret One", sans-serif; font-size: 6.5px; color: var(--blue); margin-top: 4px; }
  .mini-cover .mini-dancer {
    position: absolute; left: 36px; top: 70px; width: 96px; height: 118px; border-radius: 40% 50% 30% 45%;
    background: radial-gradient(ellipse at 50% 55%, var(--silk), #2f3d55 60%, transparent 75%);
  }
  .series-block { position: absolute; left: 223px; top: 53px; width: 225px; font-size: 9.5px; line-height: 1.3; }
  .series-block h1 { font-size: 19.5px; color: var(--blue); font-weight: 400; margin-bottom: 2px; }
  .series-block .label { color: var(--blue); }
  .series-block p + p { margin-top: 11px; }

  .about h2 { font-size: 17.5px; color: var(--blue); font-weight: 400; margin-bottom: 5px; }
  .about p { font-size: 7.4px; line-height: 1.43; }
  .about p + p { margin-top: 10px; }
  .about-dancer { position: absolute; left: 37px; top: 279px; width: 215px; }
  .about-photographer { position: absolute; left: 37px; top: 468px; width: 400px; }
  .portrait-photo {
    position: absolute; left: 265px; top: 284px; width: 170px; height: 168px;
    transform: rotate(3deg);
    background: radial-gradient(ellipse at 45% 60%, #cfc8bd 0%, #6d675f 35%, #1a1816 70%);
  }

  /* ---------- Front cover ---------- */
  .front-cover { position: absolute; left: 460px; top: 0; width: 460px; height: 595px; background: radial-gradient(ellipse at 55% 60%, var(--night-soft), var(--night) 70%); }
  .front-cover h1 { position: absolute; left: 40px; top: 52px; font-size: 43px; font-weight: 400; color: var(--blue); }
  .front-cover h1 span { color: #fff; }
  .front-cover .flourish { position: absolute; left: 40px; top: 143px; width: 76px; height: 9px; background: #a9b7c8; opacity: .7; border-radius: 4px; }
  .front-cover .attribution { position: absolute; left: 40px; top: 162px; font-size: 16.5px; color: var(--blue); }
  .front-cover .dancer {
    position: absolute; left: 45px; top: 175px; width: 380px; height: 340px;
    background: radial-gradient(ellipse at 50% 55%, #7d9cc2 0%, #48618a 35%, rgba(40,48,64,.6) 58%, transparent 72%);
  }

  /* ---------- Inside spread ---------- */
  .essay { position: absolute; top: 638px; }
  .essay-left { left: 30px; width: 420px; }
  .essay-right { left: 493px; width: 390px; }
  .essay section { position: relative; padding-left: 18px; }
  .essay section + section { margin-top: 16px; }
  .essay h2 { font-size: 17.5px; color: var(--blue); font-weight: 400; margin-bottom: 4px; }
  .essay .scroll { position: absolute; left: 2px; top: 2px; width: 6px; height: 30px; background: var(--blue); opacity: .55; border-radius: 3px; }
  .essay p { font-size: 9.6px; line-height: 1.28; }
  .essay p + p { margin-top: 11px; }
  .essay .lead-quote { color: var(--blue-deep); }

  .circles { position: absolute; left: 0; top: 0; width: 920px; height: 1200px; pointer-events: none; }

  .full-quote { position: absolute; left: 510px; top: 926px; width: 372px; font-size: 9.6px; line-height: 1.3; color: var(--blue-deep); }

  .closing-band { position: absolute; left: 460px; top: 1030px; width: 460px; height: 170px; background: var(--band); color: #fff; padding: 20px 50px 0 50px; }
  .closing-band .flourish { width: 76px; height: 9px; background: #dfe8f2; opacity: .6; border-radius: 4px; margin-bottom: 9px; }
  .closing-band p { font-size: 9.6px; line-height: 1.3; }
  .closing-band p + p { margin-top: 11px; }
</style>
</head>
<body>

<!-- Back cover -->
<div class="back-cover">
  <div class="mini-cover">
    <div class="mini-title display">There will <span>only</span><br>ever be <span>one</span></div>
    <div class="mini-attr">- EDITH SORREL</div>
    <div class="mini-dancer" role="img" aria-label="Reduced cover photo of a leaping dancer in a blue silk dress"></div>
  </div>

  <div class="series-block">
    <h1 class="display">There will only ever be one you</h1>
    <p>is the 16th in a series of Labor Day essays inviting a moment of reflection on living a more meaningful, more mindful life</p>
    <p><span class="label">Nora Vellacott, Ph.D.</span><br>Heron Gate House<br>18 Orchard Lane<br>Millbrook Falls, Vermont&nbsp; 05999</p>
    <p><span class="label">Mobile:</span>&nbsp; 555-014-2286<br><span class="label">Email:</span> nvellacott@mailhaven.net</p>
  </div>

  <div class="about about-dancer">
    <h2 class="display">About Edith Sorrel</h2>
    <p>Born in 1894, Edith Sorrel danced and taught for over 70 years. She is recognized as a primal artistic force of the 20th century, whose influence on modernity has been compared to Aurel Fenn, Miles Caddow, Tomas Brevik, and Owen Marsh Hale. Her themes dealt with the lives and conflicts of ordinary people, and she brought serious issues to the stage like war, poverty, intolerance and the injustices of slavery and treatment of Native Americans.</p>
    <p>Rebelling against conventions of the past, her dancing and choreography exposed the depths of human emotion through intense movements that were forceful, stark, angular, jagged, and percussive – startlingly unlike the formality of classical ballet, which she saw as antiquated.</p>
  </div>
  <div class="portrait-photo" role="img" aria-label="Black and white photograph of a dancer in a flowing white dress, arm raised"></div>

  <div class="about about-photographer">
    <h2 class="display">About the Photographer</h2>
    <p>In 1935 Clara Winslow saw a performance by modern dancer and choreographer Edith Sorrel. Winslow was so inspired by the dance performance that she introduced herself to Sorrel, and the two artists began an artistic collaboration that lasted more than 60 years. Winslow often photographed dancers in action, to capture the emotion behind their movement. Her artistic style was in line with Sorrel’s philosophy of dance. This photo from the dance, “Note to the Morning,” is one of Winslow’s most famous photographs. The title of this work comes from a Harriet Alden poem, which inspired Sorrel to create a dance performance based on Alden’s life.</p>
  </div>
</div>

<!-- Front cover -->
<div class="front-cover">
  <h1 class="display">There will <span>only</span><br>ever be <span>one you</span>!</h1>
  <div class="flourish" role="img" aria-label="Small decorative flourish"></div>
  <div class="attribution display">- Edith Sorrel</div>
  <div class="dancer" role="img" aria-label="Photograph of a barefoot dancer leaping in a blue silk dress against a dark smoky background"></div>
</div>

<!-- Inside spread, left page -->
<div class="essay essay-left">
  <section>
    <div class="scroll" role="img" aria-label="Decorative scroll ornament"></div>
    <h2 class="display">In the rural<br>Ohio village</h2>
    <p>where I grew up, one of the highlights of Sunday morning church service -- in between congregational hymn-singing and the preacher’s sermon -- was the “special selection,” a musical performance by a parishioner. Typically, it was a vocalist or instrumental on piano, organ or violin.</p>
  </section>
  <section>
    <div class="scroll" role="img" aria-label="Decorative scroll ornament"></div>
    <h2 class="display">One Sunday, we<br>were surprised</h2>
    <p>by an unusual performance. A plump, buxom farm wife approached the pulpit, puckered up her lips and unexpectedly began to whistle the hymn “The Old Willow Hill.” As a 10-year-old, I found this hilarious as I tried to choke back my wide-eyed</p>
  </section>
  <section>
    <div class="scroll" role="img" aria-label="Decorative scroll ornament"></div>
    <h2 class="display">Despite the<br>irreverence</h2>
    <p>of my pre-adolescent reaction, this memory has stayed with me for decades as an iconic example of the wonderment of individual differences. Of the delight I find in witnessing someone express herself in sometimes surprising and even courageous ways. Of the marvel of beholding a person be truly authentic and uniquely original.</p>
  </section>
  <section>
    <div class="scroll" role="img" aria-label="Decorative scroll ornament"></div>
    <h2 class="display">Someone who personified<br>the irrepressible impulse</h2>
    <p>to express her individuality was the early 20th century dancer and choreographer Edith Sorrel. A pioneer of modern dance, she threw tradition overboard and was inspired to dance in a way that was a radical departure from the formalized style and rigidly dictated forms of classical ballet.</p>
  </section>
  <section>
    <div class="scroll" role="img" aria-label="Decorative scroll ornament"></div>
    <h2 class="display">Sorrel felt<br>compelled to</h2>
    <p>express the rawness and emotion of human experience in her dancing -- not just present a form of pretty entertainment. Iconoclastically brilliant, she created a new language of dance, a revolutionary vocabulary of movement that electrified the stage, often creating a visceral response in the audience.</p>
  </section>
</div>

<!-- Inside spread, right page -->
<div class="essay essay-right">
  <section>
    <div class="scroll" role="img" aria-label="Decorative scroll ornament"></div>
    <h2 class="display">In her biography<br>of Sorrel,</h2>
    <p>her friend and equally talented choreographer Vera Lindqvist recalled that despite sensational reviews for her own innovative work in the Broadway musical Prairie Song!, Lindqvist had a gnawing feeling that her work was only mediocre.</p>
    <p>Lindqvist confessed her anxieties to Sorrel who listened quietly and then responded, <span class="lead-quote">“There will only ever be one you!”</span> Continuing, she added:</p>
  </section>
</div>

<svg class="circles" viewBox="0 0 920 1200" aria-hidden="false">
  <defs>
    <radialGradient id="silk" cx="50%" cy="50%" r="55%">
      <stop offset="0" stop-color="#7a8fa8"/>
      <stop offset="0.6" stop-color="#9aa8b8"/>
      <stop offset="1" stop-color="#c4ccd5"/>
    </radialGradient>
    <radialGradient id="silk-warm" cx="50%" cy="45%" r="55%">
      <stop offset="0" stop-color="#8a7a6a"/>
      <stop offset="0.55" stop-color="#a9a7a4"/>
      <stop offset="1" stop-color="#c9cdd2"/>
    </radialGradient>
  </defs>
  <g role="img" aria-label="Three circular close-up crops of the leaping dancer: skirt, torso and flying hair">
    <circle cx="560" cy="839" r="47" fill="url(#silk)" stroke="#8ab0d2" stroke-width="2.5"/>
    <circle cx="662" cy="842" r="55" fill="url(#silk)" stroke="#8ab0d2" stroke-width="2.5"/>
    <circle cx="794" cy="838" r="78" fill="url(#silk-warm)" stroke="#8ab0d2" stroke-width="2.5"/>
  </g>
</svg>

<p class="full-quote">“There is a vitality, a life-force, an energy, a quickening that is translated through you into action. And because there is only one of you in all of time, this expression is unique. And if you block it, the world will not have it. It is not your business to determine how good it is nor how valuable nor how it compares with other expressions. It is your business to keep it yours clearly and directly, to keep the channel open. You have to keep open and aware directly to the urges that motivate you. Above all else, keep the channel open!”</p>

<div class="closing-band">
  <div class="flourish" role="img" aria-label="Small decorative flourish"></div>
  <p>Sorrel’s wisdom reminds us that we must not hold back or judge our gifts. Although there may be moments when we doubt ourselves or when we worry that we’re not good enough, our job is to be fearless and to “keep the channel open.” Guard the precious miracle of your own uniqueness.</p>
  <p>Find that home-sweet-home feeling where you feel you are your most authentic self. There will only ever be one you! And importantly, respect the differences of others. Our world would be a drab, boring place if we all only whistled one tune.</p>
</div>

</body>
</html>
```